Downloadable PDF "Brochure?"

We have a Free download we will provide in exchange for an email address on our new Trailcrest website. The website at www.venturetrailcrest-example.com is in development and will look nothing like what it currently does, but you can go there and get a sense of what Trailcrest is from the text on the website. (see the attached image 'site design' for the new redesigned website for aesthetics).

We are looking for a nice design for the document, that will represent the mostly text document well. We are not actually looking to print these at a printer so they don't have to be print ready. I went ahead and included the logo and colors and fonts file again just for reference.

Target Market(s)

Business Owners / Decision Makers

Requirements
Must have
• See attached document 'trailcrest freebie' for text to be utilized in the finished deliverable.
• See the attached image 'Site Design' for the website aesthetic.

```html
<!DOCTYPE html>
<html lang="en">
<head>
<meta charset="utf-8">
<title>Trailcrest – 10 Questions To Choose The Best Technology Advisor</title>
<link rel="stylesheet" href="https://fonts.googleapis.com/css2?family=Marcellus+SC&family=Open+Sans:ital,wght@0,400;0,600;0,700;1,700&display=swap">
<style>
  :root{
    --slate:#3a4951;
    --rust:#c7784b;
    --backdrop:#c3bdbd;
    --paper:#ffffff;
    --ink:#3f3f3f;
    --rule:#d9a58a;
  }
  *{box-sizing:border-box;margin:0;padding:0}
  html,body{width:1200px;height:1200px;overflow:hidden;background:var(--backdrop)}
  .spread{position:relative;width:1500px;height:1500px;transform:scale(.8);transform-origin:0 0}
  .page{position:absolute;background:var(--paper);box-shadow:2px 3px 5px rgba(0,0,0,.28);overflow:hidden;font-family:"Open Sans",Arial,sans-serif;color:var(--ink)}
  .page--cover{left:217px;top:91px;width:498px;height:644px}
  .page--two{left:759px;top:91px;width:495px;height:647px}
  .page--three{left:39px;top:789px;width:450px;height:583px}
  .page--four{left:524px;top:789px;width:450px;height:583px}
  .page--five{left:1006px;top:789px;width:449px;height:583px}

  .masthead{position:absolute;left:0;top:0;width:100%;display:block}
  .page--cover .masthead,.page--two .masthead{height:112px}
  .page--three .masthead,.page--four .masthead,.page--five .masthead{height:102px}

  .brand{position:absolute;font-family:"Open Sans",Arial,sans-serif;font-weight:600;color:var(--slate);text-align:right;line-height:1;letter-spacing:.3px}
  .page--cover .brand,.page--two .brand{right:32px;top:142px;font-size:17px}
  .page--three .brand,.page--four .brand,.page--five .brand{right:28px;top:128px;font-size:15px}

  .rule{position:absolute;left:0;width:100%;height:1px;background:var(--rule)}
  .page--cover .rule{top:282px}
  .page--two .rule{top:181px}
  .page--three .rule,.page--four .rule,.page--five .rule{top:164px}

  .title{position:absolute;left:26px;top:192px;display:flex;align-items:center;color:var(--slate);font-weight:400}
  .title__num{font-family:"Marcellus SC",Georgia,serif;font-size:72px;color:var(--rust);line-height:1;margin-right:12px;letter-spacing:-2px}
  .title__text{font-family:"Marcellus SC",Georgia,serif;font-size:28px;line-height:29px;letter-spacing:.6px}

  .column{position:absolute}
  .page--cover .column{left:132px;top:294px;width:338px;font-size:9.1px;line-height:12.9px;letter-spacing:-.1px}
  .page--two .column{left:131px;top:191px;width:334px;font-size:9.1px;line-height:12.9px;letter-spacing:-.1px}
  .page--three .column{left:119px;top:173px;width:306px;font-size:8.1px;line-height:11.7px;letter-spacing:-.1px}
  .page--four .column{left:128px;top:174px;width:298px;font-size:8.1px;line-height:11.7px;letter-spacing:-.1px}
  .page--five .column{left:119px;top:175px;width:302px;font-size:8.1px;line-height:11.7px;letter-spacing:-.1px}

  .intro{font-weight:700;color:#3d3d3d;line-height:14.5px;margin-bottom:10px}
  .intro__cap{float:left;font-family:"Marcellus SC",Georgia,serif;font-size:58px;line-height:44px;color:var(--rust);margin:3px 6px 0 0}
  .question{font-weight:700;color:var(--rust)}
  .answer{margin-bottom:11px}
  .page--three .answer,.page--four .answer,.page--five .answer{margin-bottom:10px}
  .reading{font-weight:700;font-style:italic}

  .footer{position:absolute;left:0;bottom:0;width:100%;height:26px;display:block}
  .page--three .footer,.page--four .footer,.page--five .footer{height:24px}
  .folio{position:absolute;right:30px;bottom:7px;font-size:9px;font-weight:700;color:#fff}
  .page--three .folio,.page--four .folio,.page--five .folio{bottom:6px;font-size:8px}
</style>
</head>
<body>
<div class="spread">

  <article class="page page--cover">
    <svg class="masthead" viewBox="0 0 500 112" preserveAspectRatio="none" aria-hidden="true">
      <path fill="var(--rust)" d="M0 72 C60 86 140 104 230 90 C320 76 400 34 460 46 C480 52 492 64 500 72 V92 C490 78 478 64 458 58 C398 46 320 88 230 102 C140 114 60 98 0 84 Z"/>
      <path fill="var(--slate)" d="M0 0 H500 V72 C492 64 480 52 460 46 C400 34 320 76 230 90 C140 104 60 86 0 72 Z"/>
    </svg>
    <div class="brand">Trailcrest</div>
    <h1 class="title"><span class="title__num">10</span><span class="title__text">Questions To Choose The<br>Best Technology Advisor</span></h1>
    <div class="rule"></div>
    <div class="column">
      <p class="intro"><span class="intro__cap">W</span>hen you choose a technology advisor whether it be a Managed Service Provider, fractional CIO or a full-time CIO you need to make sure that they understand business just as much as they understand technology. Some of the biggest complaints about the IT department are that they just don’t “Get it”. The questions below should help you determine whether or not they have a technology mindset or a business mindset.</p>
      <p class="question">What is scalability? How important is it from a technology perspective on a scale of 1-&gt;10 with 10 being the highest? What all does scalability impact?</p>
      <p class="answer">This question is designed to get a reading on the person’s mindset. A typical technology-minded response would be something describing the ability of systems or software to scale by adding additional resources. When working from a business point of view, however, you want to see it defined as the ability for the organization to support increased volume without sacrificing margins. The importance of this concept cannot be overstated and should be a 9 or 10 in terms of ranking. Regarding impact, you want to see not just an understanding of having to spend money two or three times for a different solution to the same problem, but an acknowledgment of the ‘total’ cost, including adoption fatigue, the opportunity cost of change, and the competitive disadvantage it creates. For concepts of business scalability refer to <span class="reading">‘Growing Steady’ by Corin Vale</span>.</p>
    </div>
    <svg class="footer" viewBox="0 0 500 26" preserveAspectRatio="none" aria-hidden="true">
      <rect width="500" height="26" fill="var(--slate)"/>
      <path fill="var(--rust)" d="M0 0 H246 L252 13 L246 26 H0 Z"/>
    </svg>
    <span class="folio">Pg.1</span>
  </article>

  <article class="page page--two">
    <svg class="masthead" viewBox="0 0 500 112" preserveAspectRatio="none" aria-hidden="true">
      <path fill="var(--rust)" d="M0 72 C60 86 140 104 230 90 C320 76 400 34 460 46 C480 52 492 64 500 72 V92 C490 78 478 64 458 58 C398 46 320 88 230 102 C140 114 60 98 0 84 Z"/>
      <path fill="var(--slate)" d="M0 0 H500 V72 C492 64 480 52 460 46 C400 34 320 76 230 90 C140 104 60 86 0 72 Z"/>
    </svg>
    <div class="brand">Trailcrest</div>
    <div class="rule"></div>
    <div class="column">
      <p class="question">Provide an example where you solved a problem without the use of technology.</p>
      <p class="answer">Often technology-minded individuals become so wrapped up in the solutions themselves they fail to realize a policy or process change is far more effective and simple than making changes to existing or introducing new technology. Asking for a specific example here should demonstrate the ability to think from a business mindset. For specific examples reference <span class="reading">‘The Lantern Initiative’ by Dorn, Avery, and Lisk.</span></p>
      <p class="question">How do you go about prioritizing solutions in order of importance for implementation / adoption?</p>
      <p class="answer">Answers here should include reference to some form of discovery process or a thorough evaluation at the operations level. One of the key skill sets for someone approaching technology from a business point of view is mapping solutions and their respective importance to business outcomes and (often more importantly) eliminating bottlenecks while respecting that some implementations must necessarily come before others to be viable. For reference on the Theory of Constraints see <span class="reading">‘The Throughput’ by Halvard Menz.</span></p>
      <p class="question">What is Information Technology Debt?</p>
      <p class="answer">Stated simply, ‘IT Debt’ is a measurement of the out-of-date, incomplete or yet-to-be-defined technology changes. Debt occurs for a number of reasons, including lack of qualified personnel to implement the needed solutions (or recognize the problem in the first place); historical spending haunting the organization “we spent money on something like this before and look what it got us”; Fire-fighting (addressing issues purely reactively in a downward spiral leaving no time for fixing the real underlying problem); or most commonly, the budget being already allocated to other company endeavors that seem immediately more pressing. By recognizing what IT Debt is, the individual demonstrates an acknowledgment of how impactful it can be when neglected and not brought to the forefront of business planning sessions.</p>
    </div>
    <svg class="footer" viewBox="0 0 500 26" preserveAspectRatio="none" aria-hidden="true">
      <rect width="500" height="26" fill="var(--slate)"/>
      <path fill="var(--rust)" d="M0 0 H250 L256 13 L250 26 H0 Z"/>
    </svg>
    <span class="folio">Pg.2</span>
  </article>

  <article class="page page--three">
    <svg class="masthead" viewBox="0 0 500 112" preserveAspectRatio="none" aria-hidden="true">
      <path fill="var(--rust)" d="M0 72 C60 86 140 104 230 90 C320 76 400 34 460 46 C480 52 492 64 500 72 V92 C490 78 478 64 458 58 C398 46 320 88 230 102 C140 114 60 98 0 84 Z"/>
      <path fill="var(--slate)" d="M0 0 H500 V72 C492 64 480 52 460 46 C400 34 320 76 230 90 C140 104 60 86 0 72 Z"/>
    </svg>
    <div class="brand">Trailcrest</div>
    <div class="rule"></div>
    <div class="column">
      <p class="question">Provide an example where you argued against implementing a technology solution and why.</p>
      <p class="answer">Despite it being seemingly obvious, using ‘outside of budget’ is not a good answer. Business-minded technology advisors should be intimately aware of how well a proposed solution will integrate into the existing company ecosystem (software tools already present, workflow, and processes), if it drives the company toward reducing/eliminating a bottleneck (and thereby creates more leverage), and if it fits the company’s culture. If any of these are a no, the solution should be carefully examined for what it really offers the organization. If yes, the budget should be evaluated as a cost-benefit analysis, not a flat number ‘not to exceed’.</p>
      <p class="question">What is your ideal method for maintaining technology alignment for the company?</p>
      <p class="answer">You want to see a specific process envisioned here. At the very least a recommendation to be involved in business planning meetings or retreats, and ideally a standing technology focused meeting with leadership present should be argued for. For technology to be truly in alignment, it must fit the needs of the organization, not the other way around. This needs to come from the top level, and it means a representative must be present in critical business strategy meetings to understand where the company is headed, what operational constraints they are encountering, and what their short-term goals are. For an outline of how this model has been the underlying key to success for several well-known companies reference <span class="reading">‘Built to Endure’ by Tamsin Rook.</span></p>
      <p class="question">How do you plan on measuring and monitoring the adoption success of a solution or project?</p>
      <p class="answer">Technically minded individuals often look at the point of ‘it’s up and running and it all works’, as where their responsibilities end. Someone with a business mindset should demonstrate that evaluating how well the solution has been adopted into the day to day workflow, and to what degree</p>
    </div>
    <svg class="footer" viewBox="0 0 500 26" preserveAspectRatio="none" aria-hidden="true">
      <rect width="500" height="26" fill="var(--slate)"/>
      <path fill="var(--rust)" d="M0 0 H250 L256 13 L250 26 H0 Z"/>
    </svg>
    <span class="folio">Pg.3</span>
  </article>

  <article class="page page--four">
    <svg class="masthead" viewBox="0 0 500 112" preserveAspectRatio="none" aria-hidden="true">
      <path fill="var(--rust)" d="M0 72 C60 86 140 104 230 90 C320 76 400 34 460 46 C480 52 492 64 500 72 V92 C490 78 478 64 458 58 C398 46 320 88 230 102 C140 114 60 98 0 84 Z"/>
      <path fill="var(--slate)" d="M0 0 H500 V72 C492 64 480 52 460 46 C400 34 320 76 230 90 C140 104 60 86 0 72 Z"/>
    </svg>
    <div class="brand">Trailcrest</div>
    <div class="rule"></div>
    <div class="column">
      <p class="answer">the solution has increased leverage or operational transparency are the true critical indicators of success. There should be a specific process of follow-up after implementation to flag adoption or workflow issues due to problems such as inadequate training, unforeseen incompatibilities (whether they be process or technology related), or simply resistance to change. These findings can then be brought back to leadership to evaluate how best to improve successful adoption going forward.</p>
      <p class="question">Provide an example where you had to balance customer and employee technology experience with security and compliance.</p>
      <p class="answer">A critical role fulfilled by a technology advisor is being able to balance maintaining compliance and sound security practices with as painless of a technology experience as possible. They should be able to weigh the critical importance of protecting the organization from the negative public relations and liability of a security flaw while respecting a solution must be usable to be useful. Look for an example that demonstrates an understanding of both sides and strikes a balance without going to an extreme in either direction.</p>
      <p class="question">What would you do first, if you were selected as our advisor? Can you give me details on what your discovery or on-boarding process includes?</p>
      <p class="answer">You are looking to make sure that they don’t stop at the technology. There should be a higher focus on understanding what the company processes are and how the people inside the organization get work done. If they focus only on network, security, and disaster recovery assessments then they do not have a business mindset.</p>
    </div>
    <svg class="footer" viewBox="0 0 500 26" preserveAspectRatio="none" aria-hidden="true">
      <rect width="500" height="26" fill="var(--slate)"/>
      <path fill="var(--rust)" d="M0 0 H250 L256 13 L250 26 H0 Z"/>
    </svg>
    <span class="folio">Pg.4</span>
  </article>

  <article class="page page--five">
    <svg class="masthead" viewBox="0 0 500 112" preserveAspectRatio="none" aria-hidden="true">
      <path fill="var(--rust)" d="M0 72 C60 86 140 104 230 90 C320 76 400 34 460 46 C480 52 492 64 500 72 V92 C490 78 478 64 458 58 C398 46 320 88 230 102 C140 114 60 98 0 84 Z"/>
      <path fill="var(--slate)" d="M0 0 H500 V72 C492 64 480 52 460 46 C400 34 320 76 230 90 C140 104 60 86 0 72 Z"/>
    </svg>
    <div class="brand">Trailcrest</div>
    <div class="rule"></div>
    <div class="column">
      <p class="question">Can you give me an example of a time you gave a suggestion for a solution and it was not taken? Describe the solution and why it was important to the organization. And why do you think they didn’t implement it?</p>
      <p class="answer">When they describe why they think the solution was important do they simply talk about risk reduction or uptime improvements without tying them back to an organizational goal or bottleneck. Being able to demonstrate actual business value is a critical skill for a technology advisor. For reference on technical excellence in service of business objectives rather than blindly servicing requirements see <span class="reading">‘A Voice in the Room’ by Ellis Marrow.</span></p>
    </div>
    <svg class="footer" viewBox="0 0 500 26" preserveAspectRatio="none" aria-hidden="true">
      <rect width="500" height="26" fill="var(--slate)"/>
      <path fill="var(--rust)" d="M0 0 H250 L256 13 L250 26 H0 Z"/>
    </svg>
    <span class="folio">Pg.5</span>
  </article>

</div>
</body>
</html>
```